Website Redesign - Money is Guaranteed!

I would like a site similar to this: http://www.givewheelsforheroes.example

old site: http://www.autosforpatriots.example

Create a professional website; a car donation site seeking leads to return calls.

Please see http://www.givewheelsforheroes.example for the concept I am after.

The webpage should have a professional feel. The pages to include are 'Home', 'About us' and 'Get Started'

Industry/Entity Type

It Professional

Coding

Coded - Design and coding required

Number of Pages Required

1 page

```html
<!DOCTYPE html>
<html lang="en">
<head>
<meta charset="utf-8">
<title>Autos For Patriots – Donate Your Car</title>
<link rel="stylesheet" href="https://fonts.googleapis.com/css2?family=Open+Sans:wght@400;600;700;800&display=swap">
<style>
:root{
  --navy:#0f2a6e;
  --navy-deep:#0a1f55;
  --red:#a3140f;
  --red-bright:#b81c18;
  --gold:#b08a3e;
  --ink:#1c1c1c;
  --muted:#3a3a3a;
  --page:#e9e9ea;
  --line:#cfcfcf;
  --white:#ffffff;
}
*{box-sizing:border-box;margin:0;padding:0}
html,body{width:1200px;height:2442px;overflow:hidden}
body{background:var(--page);font-family:"Open Sans",Arial,sans-serif;color:var(--ink);position:relative}
.page{position:absolute;left:15px;top:15px;width:1170px;height:2411px;background:var(--white);overflow:hidden}
.abs{position:absolute}

/* header */
.site-header{left:0;top:0;width:1170px;height:151px;background:linear-gradient(100deg,#1d3a8a 0%,#28479a 40%,#c9ced8 70%,#e8e2e0 100%)}
.brand{left:35px;top:58px;display:flex;align-items:center;gap:12px}
.brand-mark{width:34px;height:34px;background:var(--red);border-radius:4px}
.brand-name{font-weight:800;font-size:27px;color:var(--white);letter-spacing:.5px}
.call-box{left:775px;top:0;width:395px;height:151px;background:var(--red);display:flex;align-items:center;padding-left:20px;gap:16px;color:var(--white)}
.call-icon{width:64px;height:64px;border:3px solid var(--white);border-radius:50%;display:flex;align-items:center;justify-content:center;flex:none}
.call-text .label{font-weight:700;font-size:19px;line-height:1.1}
.call-text .phone{font-weight:800;font-size:29px;line-height:1.15}
.call-text .hours{font-weight:700;font-size:13px}

.main-nav{left:0;top:151px;width:761px;height:46px;background:var(--red-bright);display:flex;align-items:center;padding-left:172px;gap:46px}
.main-nav a{color:var(--white);font-weight:700;font-size:15px;text-decoration:none}
.form-tab{left:761px;top:151px;width:378px;height:46px;background:var(--white);display:flex;align-items:center;justify-content:center;color:var(--red);font-weight:800;font-size:18px}
.form-tab .tab-dot{position:absolute;left:174px;top:-14px;width:30px;height:30px;border-radius:50%;background:var(--red);display:flex;align-items:center;justify-content:center}

/* hero */
.hero-photo{left:0;top:197px;width:1170px;height:388px;background:linear-gradient(90deg,#8a7a62 0%,#c7c3bd 35%,#d9d7d6 55%,#e6e0dd 100%)}
.donate-form{left:775px;top:197px;width:350px;height:388px;background:var(--red);padding:24px 16px 0}
.donate-form h2{color:var(--white);font-size:16.5px;font-weight:700;text-align:center;margin-bottom:11px}
.field-row{display:flex;gap:9px;margin-bottom:8px}
.field{flex:1;height:29px;background:var(--white);border-radius:3px;font-size:11.5px;font-weight:600;color:#333;display:flex;align-items:center;justify-content:space-between;padding:0 8px}
.field .caret{border:5px solid transparent;border-top:6px solid #555;margin-top:5px}
.btn-donate{display:inline-flex;margin-top:6px;width:154px;height:39px;background:var(--navy);color:var(--white);font-weight:700;font-size:15px;align-items:center;justify-content:center;border-radius:3px}

/* benefit band */
.benefit-band{left:0;top:585px;width:1170px;height:193px;background:linear-gradient(180deg,#e3e3e4,#cfd0d2);box-shadow:0 10px 12px -8px rgba(0,0,0,.35)}
.band-title{left:57px;top:28px;font-weight:800;line-height:1}
.band-title .l1{color:var(--red);font-size:30px;display:block}
.band-title .l2{color:var(--gold);font-size:54px;display:block;margin:10px 0 8px;letter-spacing:1px}
.band-title .l3{color:var(--navy);font-size:30px;display:block}
.benefit{top:40px;width:130px;text-align:center;color:var(--red);font-weight:700;font-size:12.5px;line-height:1.25}
.benefit svg{display:block;margin:0 auto 14px}

/* section titles */
.section-title{left:0;width:1170px;text-align:center;font-weight:800;font-size:30px;color:var(--navy)}
.section-title span{color:var(--red)}
.section-title .rule{display:inline-block;vertical-align:middle;width:90px;height:1px;background:var(--line);margin:0 26px}

/* how */
.step{top:973px;width:340px;display:flex;gap:20px}
.step h3{font-size:14.5px;font-weight:800;color:var(--navy);line-height:1.25;margin:15px 0 12px}
.step p{font-size:13.5px;font-weight:600;color:var(--muted);line-height:1.45}

/* why */
.why{left:0;top:1130px;width:1170px;height:405px;background:linear-gradient(90deg,#f6f2ef 0%,#ece6e2 45%,#dcd3cc 70%,#b9a899 100%)}
.why-list{left:34px;top:128px;list-style:none}
.why-list li{display:flex;align-items:center;gap:12px;height:32.5px;font-size:13.5px;color:var(--ink)}
.why-list b{font-weight:700}
.bullet{width:24px;height:24px;border-radius:50%;background:var(--red);display:flex;align-items:center;justify-content:center;flex:none}

/* faq */
.faq-photo{left:78px;top:1665px;width:506px;height:415px;background:linear-gradient(180deg,#b8323a 0%,#e8e6ea 40%,#8a7658 80%,#6b6a6c 100%)}
.faq-list{left:617px;top:1665px;width:475px}
.faq-item{border:1px solid #c9c9c9;border-radius:8px;margin-bottom:7px;padding:0 15px;height:39px;display:flex;align-items:center;justify-content:space-between;font-weight:700;font-size:14.5px;color:#333}
.faq-item.open{height:135px;display:block;padding-top:10px}
.faq-item.open .q{display:flex;justify-content:space-between}
.faq-item.open p{font-weight:400;font-size:13px;line-height:1.5;color:#555;margin-top:6px}

/* footer */
.site-footer{left:0;top:2134px;width:1170px;height:252px;background:linear-gradient(90deg,#0c2466,#1a3a8c 50%,#12306e)}
.footer-brand{left:34px;top:108px;display:flex;align-items:center;gap:12px}
.footer-col{top:42px;color:var(--white)}
.footer-col h4{font-size:14px;font-weight:800;padding-bottom:10px;border-bottom:1px solid rgba(255,255,255,.5);margin-bottom:14px}
.footer-col p{font-size:12.5px;font-weight:600;line-height:1.5}
.footer-col ul{list-style:none;font-size:12.5px;font-weight:700;line-height:1.55}
.footer-call{left:866px;top:37px;width:280px;height:118px;border:2px solid var(--white);border-radius:6px;color:var(--white);text-align:center;padding-top:18px}
.footer-call .label{font-weight:700;font-size:19px}
.footer-call .phone{font-weight:800;font-size:29px;line-height:1.1}
.footer-call .hours{font-weight:700;font-size:13px}
.legal-bar{left:0;top:2386px;width:1170px;height:25px;background:var(--red);color:var(--white);font-size:11.5px;font-weight:700;display:flex;align-items:center;justify-content:center}
</style>
</head>
<body>
<div class="page">

  <header class="site-header abs" role="img" aria-label="Waving American flag background">
  </header>
  <div class="brand abs"><span class="brand-mark"></span><span class="brand-name">AUTOS FOR PATRIOTS</span></div>
  <div class="call-box abs">
    <div class="call-icon">
      <svg width="32" height="32" viewBox="0 0 24 24"><path fill="#fff" d="M6.6 10.8a15.1 15.1 0 0 0 6.6 6.6l2.2-2.2c.3-.3.7-.4 1-.2 1.1.4 2.3.6 3.6.6.6 0 1 .4 1 1V20c0 .6-.4 1-1 1A17 17 0 0 1 3 4c0-.6.4-1 1-1h3.5c.6 0 1 .4 1 1 0 1.3.2 2.5.6 3.6.1.3 0 .7-.2 1z"/></svg>
    </div>
    <div class="call-text">
      <div class="label">CALL TODAY TO DONATE</div>
      <div class="phone">1-800-555-0142</div>
      <div class="hours">Live Operators Available - 7 Days A Week</div>
    </div>
  </div>

  <nav class="main-nav abs">
    <a href="#how">HOW TO DONATE</a><a href="#why">WHY DONATE</a><a href="#faq">FAQ</a><a href="#about">ABOUT</a>
  </nav>

  <div class="hero-photo abs" role="img" aria-label="Soldier hugging a child holding a small flag beside a red classic car, city skyline behind"></div>

  <div class="form-tab abs">
    <span class="tab-dot"><svg width="16" height="12" viewBox="0 0 16 12"><path fill="#fff" d="M3 5l2-4h6l2 4h1v5h-2v2h-2v-2H6v2H4v-2H2V5z"/></svg></span>
    DONATE YOUR CAR ONLINE
  </div>
  <form class="donate-form abs">
    <h2>Full Tax Deduction - Running or Not</h2>
    <div class="field-row"><div class="field">First Name</div><div class="field">Last Name</div></div>
    <div class="field-row"><div class="field">Daytime Phone</div><div class="field">Email</div></div>
    <div class="field-row"><div class="field">Pickup Address</div></div>
    <div class="field-row"><div class="field">Pickup City</div></div>
    <div class="field-row"><div class="field">Pickup State<span class="caret"></span></div><div class="field">Zip Code</div></div>
    <div class="field-row"><div class="field">Choose Year<span class="caret"></span></div><div class="field">Choose Make<span class="caret"></span></div></div>
    <div class="field-row"><div class="field">Vehicle Model</div></div>
    <span class="btn-donate">DONATE NOW</span>
  </form>

  <section class="benefit-band abs">
    <h1 class="band-title abs"><span class="l1">DONATE YOUR CAR TO</span><span class="l2">PATRIOTS</span><span class="l3">MAKE A DIFFERENCE</span></h1>
    <div class="benefit abs" style="left:501px">
      <svg width="56" height="56" viewBox="0 0 56 56"><circle cx="28" cy="28" r="24" fill="none" stroke="#0f2a6e" stroke-width="4"/><path d="M17 28l8 8 16-18" fill="none" stroke="#0f2a6e" stroke-width="4"/></svg>
      You have<br>no costs</div>
    <div class="benefit abs" style="left:631px">
      <svg width="56" height="56" viewBox="0 0 56 56"><rect x="8" y="26" width="28" height="16" fill="#0f2a6e"/><path d="M36 30h8l6 6v6H36z" fill="#0f2a6e"/><path d="M14 26l10-18" stroke="#0f2a6e" stroke-width="3"/><circle cx="16" cy="46" r="5" fill="#fff" stroke="#0f2a6e" stroke-width="3"/><circle cx="42" cy="46" r="5" fill="#fff" stroke="#0f2a6e" stroke-width="3"/></svg>
      Free towing,<br>running or not</div>
    <div class="benefit abs" style="left:762px">
      <svg width="56" height="56" viewBox="0 0 56 56"><path d="M14 4h28v48l-5-4-4 4-5-4-5 4-4-4-5 4z" fill="none" stroke="#0f2a6e" stroke-width="3"/><path d="M20 16h16M20 34h16M20 40h16" stroke="#0f2a6e" stroke-width="2.5"/><text x="28" y="30" font-size="12" font-weight="700" fill="#0f2a6e" text-anchor="middle" font-family="Open Sans,sans-serif">$</text></svg>
      We issue you an<br>IRS tax receipt</div>
    <div class="benefit abs" style="left:890px">
      <svg width="56" height="56" viewBox="0 0 56 56"><path d="M12 4h24l8 8v40H12z" fill="none" stroke="#0f2a6e" stroke-width="3"/><circle cx="34" cy="28" r="9" fill="none" stroke="#0f2a6e" stroke-width="3"/><path d="M27 35l-9 9M18 14h12M18 20h8" stroke="#0f2a6e" stroke-width="3"/></svg>
      We take care of<br>all paperwork.</div>
    <div class="benefit abs" style="left:1017px">
      <svg width="56" height="56" viewBox="0 0 56 56"><rect x="10" y="8" width="36" height="44" rx="3" fill="none" stroke="#0f2a6e" stroke-width="3"/><rect x="20" y="4" width="16" height="8" fill="#0f2a6e"/><path d="M18 34l3-8h14l3 8v8H18z" fill="#0f2a6e"/><path d="M18 18h20" stroke="#0f2a6e" stroke-width="3"/></svg>
      We take care of<br>DMV &amp; Smog issues</div>
  </section>

  <h2 id="how" class="section-title abs" style="top:849px"><i class="rule"></i>HOW TO <span>DONATE</span><i class="rule"></i></h2>
  <div class="step abs" style="left:58px">
    <svg width="80" height="78" viewBox="0 0 80 78" style="flex:none"><rect x="14" y="0" width="46" height="14" fill="#a3140f"/><rect x="14" y="20" width="46" height="14" fill="#a3140f"/><rect x="14" y="40" width="30" height="14" fill="#a3140f"/><path d="M4 74l18-24 8 8z" fill="#a3140f"/></svg>
    <div><h3>CALL US AT 1-800-555-0142 OR<br>FILL OUT THE ONLINE FORM</h3><p>Donating your vehicle is easy and<br>donation is accepted nationwide.</p></div>
  </div>
  <div class="step abs" style="left:436px">
    <svg width="80" height="78" viewBox="0 0 80 78" style="flex:none"><rect x="6" y="22" width="26" height="22" fill="#a3140f"/><path d="M32 30h30l10 14H32z" fill="#a3140f"/><circle cx="18" cy="48" r="7" fill="#fff" stroke="#a3140f" stroke-width="3"/><circle cx="58" cy="48" r="7" fill="#fff" stroke="#a3140f" stroke-width="3"/></svg>
    <div><h3>WE TOW THE VEHICLE</h3><p>Any vehicles is accepted and we will<br>arrange to pick up your vehicle when<br>it is most convenient for you.</p></div>
  </div>
  <div class="step abs" style="left:827px">
    <svg width="80" height="78" viewBox="0 0 80 78" style="flex:none"><path d="M14 4h40v66l-6-5-7 5-6-5-7 5-7-5-7 5z" fill="none" stroke="#a3140f" stroke-width="3"/><rect x="26" y="40" width="22" height="18" fill="none" stroke="#a3140f" stroke-width="2.5"/><text x="34" y="32" font-size="20" font-weight="700" fill="#a3140f" text-anchor="middle" font-family="Open Sans,sans-serif">$</text></svg>
    <div><h3>TAX WRITE-OFF</h3><p>Once the vehicle donation is<br>complete, you will receive your<br>tax deductable vehicle donation<br>receipt.</p></div>
  </div>

  <section id="why" class="why abs" role="img" aria-label="Soldier wrapped in an American flag saluting, faded soldiers carrying a flag behind">
    <h2 class="section-title abs" style="top:72px">WHY DONATE <span>YOUR CAR TO US</span></h2>
    <ul class="why-list abs">
      <li><span class="bullet"><svg width="12" height="12" viewBox="0 0 12 12"><path d="M2 6h7M6 2l4 4-4 4" stroke="#fff" stroke-width="2" fill="none"/></svg></span><span><b>Top A+ Rated &amp; IRS 501(c)3 Approved :</b> Free 24/7 Pickup with No DMV Hassles.</span></li>
      <li><span class="bullet"><svg width="12" height="12" viewBox="0 0 12 12"><path d="M2 6h7M6 2l4 4-4 4" stroke="#fff" stroke-width="2" fill="none"/></svg></span><span><b>Free Local Towing :</b> We will pick up your car donation, running or not, when it's most convenient, at home or work.</span></li>
      <li><span class="bullet"><svg width="12" height="12" viewBox="0 0 12 12"><path d="M2 6h7M6 2l4 4-4 4" stroke="#fff" stroke-width="2" fill="none"/></svg></span><span><b>All Cars Accepted :</b> We take your car regardless of its condition or registration status.</span></li>
      <li><span class="bullet"><svg width="12" height="12" viewBox="0 0 12 12"><path d="M2 6h7M6 2l4 4-4 4" stroke="#fff" stroke-width="2" fill="none"/></svg></span><span><b>Income Tax Deduction :</b> We issue you an IRS tax receipt &amp; offer the largest resale network to get you the highest tax write-off possible.</span></li>
      <li><span class="bullet"><svg width="12" height="12" viewBox="0 0 12 12"><path d="M2 6h7M6 2l4 4-4 4" stroke="#fff" stroke-width="2" fill="none"/></svg></span><span><b>No Paperwork Hassles :</b> We take any car and handle everything: DMV, Smog and IRS paperwork.</span></li>
      <li><span class="bullet"><svg width="12" height="12" viewBox="0 0 12 12"><path d="M2 6h7M6 2l4 4-4 4" stroke="#fff" stroke-width="2" fill="none"/></svg></span><span><b>Car donations help fund programs :</b> And benefit Patriot Service Alliance. An IRS 501(c)3 nonprofit organization.</span></li>
      <li><span class="bullet"><svg width="12" height="12" viewBox="0 0 12 12"><path d="M2 6h7M6 2l4 4-4 4" stroke="#fff" stroke-width="2" fill="none"/></svg></span><span><b>Schedule a Free Pickup :</b> Complete the form and a representative will call you to arrange a convenient time to pickup your car.</span></li>
    </ul>
  </section>

  <h2 id="faq" class="section-title abs" style="top:1588px"><i class="rule"></i>FREQUENTLY ASKED <span>QUESTIONS</span><i class="rule"></i></h2>
  <div class="faq-photo abs" role="img" aria-label="American flag blended with marching soldiers' boots"></div>
  <div class="faq-list abs">
    <div class="faq-item">What types of vehicles can be donated?<svg width="12" height="8" viewBox="0 0 12 8"><path d="M1 1l5 5 5-5" stroke="#333" stroke-width="2" fill="none"/></svg></div>
    <div class="faq-item open"><div class="q">What paperwork do I need to donate my vehicle?<svg width="12" height="8" viewBox="0 0 12 8"><path d="M1 7l5-5 5 5" stroke="#333" stroke-width="2" fill="none"/></svg></div>
      <p>All you need is a title, free of all liens. We will request some general information from you at the time of donation such as, the year, make, and model of the car, as well as its general mechanical condition. We accept all vehicles, running or non-running.</p></div>
    <div class="faq-item">Is my donated vehicle tax -deductible?<svg width="12" height="8" viewBox="0 0 12 8"><path d="M1 1l5 5 5-5" stroke="#333" stroke-width="2" fill="none"/></svg></div>
    <div class="faq-item">What if the vehicle is not registered in my name?<svg width="12" height="8" viewBox="0 0 12 8"><path d="M1 1l5 5 5-5" stroke="#333" stroke-width="2" fill="none"/></svg></div>
    <div class="faq-item">How much will I receive as a tax deduction for my vehicle?<svg width="12" height="8" viewBox="0 0 12 8"><path d="M1 1l5 5 5-5" stroke="#333" stroke-width="2" fill="none"/></svg></div>
    <div class="faq-item">When will I receive my tax receipt?<svg width="12" height="8" viewBox="0 0 12 8"><path d="M1 1l5 5 5-5" stroke="#333" stroke-width="2" fill="none"/></svg></div>
    <div class="faq-item">How do I schedule a pick up?<svg width="12" height="8" viewBox="0 0 12 8"><path d="M1 1l5 5 5-5" stroke="#333" stroke-width="2" fill="none"/></svg></div>
  </div>

  <footer class="site-footer abs" role="img" aria-label="Rows of American flags background">
    <div class="footer-brand abs"><span class="brand-mark"></span><span class="brand-name">AUTOS FOR PATRIOTS</span></div>
    <div id="about" class="footer-col abs" style="left:400px;width:236px">
      <h4>ABOUT AUTOS FOR PATRIOTS</h4>
      <p>Lorem ipsum dolor sit amet, consectetuer adipiscing elit, sed diam nonummy nibheu ismod tincidunt ut laoreet dolore magna aliquam erat volutpat. Ut wisi enim ad mini veniam, quis nostrud exerci tation ullamcor per suscipit lobortis nisl ut aliquip ex ea co modo consequat.</p>
    </div>
    <div class="footer-col abs" style="left:700px;width:105px">
      <h4>NAVIGATION</h4>
      <ul><li>HOW TO DONATE</li><li>WHY DONATE</li><li>FAQ</li><li>ABOUT</li></ul>
    </div>
    <div class="footer-call abs">
      <div class="label">CALL TODAY TO DONATE</div>
      <div class="phone">1-800-555-0142</div>
      <div class="hours">Live Operators Available - 7 Days A Week</div>
    </div>
  </footer>
  <div class="legal-bar abs">COPYRIGHT © 2016 AUTOS FOR PATRIOTS. PRIVACY POLICY | TERMS &amp; CONDITIONS. ALL RIGHTS RESERVED.</div>

</div>
</body>
</html>
```